1. 商品のコンセプト:鉢植えの植物を元気にみずみずしく保つ。お客様に代わって心を込めたお手入れを。
2. 商品コンセプトの理由:水やり以外のお手入れは放置しがちな鉢植えも、お手入れすることで美しく保てることで、安らぎや楽しみを与えてくれる存在となります。
3. 販売価格:(価格はすべて税込み)
【植替え】
新しく植え替える鉢の上部直径
15㎝(5号鉢)まで 3,500円
21㎝(7号鉢)まで 6,000円
30㎝(10号鉢)まで 9,000円
45㎝(15号鉢)まで 15,000円
※ただし、盆栽は除く
●料金は作業代のみの価格となります。
●植替えで必要な鉢や土などは、お客さまがご用意いただければ別途費用がかからず、そちらを使用して作業致します。
ただし、樹種や状態によって必要な鉢のサイズや土の種類や量がありますので、お見積り時にご相談のうえご用意いただけるのが望ましいです。
●また、鉢や土など当社でご用意することも可能です。その場合、別途お見積りとなります。
●古い土は、ご希望があればお引き取りいたします(別途見積り)
●不要になった鉢のお引き取りは、ご相談ください(別途見積り)
※ただし、プラスチック、金属、ガラス、樹脂、コンクリートなどはお引き取りできません。
【剪定】形を整えたり、高さを調整したりします。
高さ3m未満 4,000円/本
【消毒】病害虫の症状にあわせた薬剤は散布し予防や駆除をします。
高さ3m未満 2,000円/本
【施肥】肥料を施して栄養分を補い、成育促進、花付き、実付きの改善をします。
3,000円より
4. 販売方法
お見積り無料
ご依頼(電話・WEB)→担当から連絡→無料見積り(お客様宅へ出向いて実際のものを見てお見積りをします。見積書有効期限1か月)→ご依頼(作業日時決定)→作業→お支払い(郵便局・銀行から振り込み、コンビニエンスストアでのお支払い(コンビニ後払い)、クレジットカード決済)

[強み]
1鉢からでも承ります。お見積り無料。お客さまご自身で植替えに必要な鉢や土などを担当者にご相談のうえご用意いただけたら、費用は作業代のみとなります(土やゴミの回収ご希望の場合は別途費用がかかります)
社名、ロゴ、電話番号、URL、QRコード
A4
両面
緑系、水色系、茶系、こだわりはそれ程強くないので、色合いはお任せします。
• イラストレーター形式 (.ai)
弊社HP
https://www.375m.co.jp/
各種メニューと価格
https://www.375m.co.jp/price/

鉢植えの植替えや鉢植えのお手入れに関する素材については、フリー素材等にて適宜入れてください。
必要に応じてリクエストさせていただきたいと思います。

必要な情報が一通り網羅されていました。
シンプルに当社のサービスを表現されていました。

短期間の中多くのご提案をいただき、誠にありがとうございました。
どのご提案もレベルが高く、良い意味で選定に苦慮しました。
また新たなチラシ作成の際は是非ご提案いただければ幸いです。

```html
<!DOCTYPE html>
<html lang="ja">
<head>
<meta charset="utf-8">
<title>植替え・お手入れサービス</title>
<link rel="stylesheet" href="https://fonts.googleapis.com/css2?family=Noto+Sans+JP:wght@400;500;700;900&family=M+PLUS+Rounded+1c:wght@500;700;800&display=swap">
<style>
:root{
  --green:#3d9a3a;
  --green-dark:#2c7a2c;
  --lime:#c9e04b;
  --lime-soft:#e6f0b8;
  --pale:#eef5dc;
  --yellow:#f3e76a;
  --ink:#2b2b2b;
  --white:#ffffff;
}
*{box-sizing:border-box;margin:0;padding:0}
html,body{width:849px;height:1200px;overflow:hidden;background:var(--white)}
body{font-family:"Noto Sans JP",sans-serif;color:var(--ink)}
.flyer{position:relative;width:849px;height:1200px;overflow:hidden;background:var(--white)}

.top-rule{position:absolute;left:0;top:60px;width:849px;height:6px;background:var(--green)}
.title-tab{position:absolute;left:283px;top:0;width:283px;height:78px;background:var(--green);color:var(--white);
  font-family:"M PLUS Rounded 1c",sans-serif;font-weight:800;font-size:40px;letter-spacing:6px;
  display:flex;align-items:center;justify-content:center;border-radius:0 0 10px 10px}

.price-panel{position:absolute;left:30px;top:92px;width:380px}
.price-lead{font-size:13px;font-weight:500;margin-bottom:12px}
.price-row{display:flex;align-items:center;height:40px;margin-bottom:10px}
.price-size{width:210px;height:40px;background:var(--lime-soft);border-left:6px solid var(--green);
  display:flex;align-items:center;padding-left:12px;font-size:18px;font-weight:700}
.price-yen{flex:1;font-size:21px;font-weight:700;text-align:right;padding-right:20px;border-bottom:2px dotted var(--green);height:40px;line-height:40px}
.price-note{font-size:14px;margin-top:8px;line-height:1.8}

.fern-photo{position:absolute;left:425px;top:85px;width:424px;height:315px;
  background:radial-gradient(circle at 55% 40%,#6fa84a 0%,#3f6e2c 45%,#1f3a18 100%)}
.free-badge{position:absolute;left:548px;top:282px;width:112px;height:112px;border-radius:50%;background:var(--yellow);
  display:flex;align-items:center;justify-content:center;text-align:center;transform:rotate(-12deg);
  font-family:"M PLUS Rounded 1c",sans-serif;font-weight:800;font-size:20px;color:var(--green-dark);line-height:1.3;
  box-shadow:0 0 0 5px var(--white)}
.one-pot{position:absolute;left:655px;top:360px;font-size:15px;font-weight:700;color:var(--white)}

.merits{position:absolute;left:14px;top:412px;width:821px;height:185px;display:flex;gap:8px}
.merit{flex:1;background:var(--pale);border-radius:6px;position:relative}
.merit svg{position:absolute}
.merit-label{position:absolute;background:var(--lime);font-weight:900;line-height:1.35;padding:7px 10px;border-radius:4px}
.merit-small{position:absolute;font-size:9.5px;line-height:1.5}

.services{position:absolute;left:14px;top:612px;width:821px;display:flex;gap:10px}
.service{flex:1}
.service-head{display:flex;align-items:center;gap:10px;height:34px}
.service-tag{background:var(--green);color:var(--white);font-weight:700;font-size:18px;padding:3px 16px;border-radius:3px;flex-shrink:0}
.service-desc{font-size:9.5px;line-height:1.35}
.service-price{margin-top:10px;background:var(--yellow);height:38px;display:flex;align-items:center;justify-content:center;gap:18px;font-size:17px;font-weight:700}

.steps{position:absolute;left:14px;top:745px;width:821px;height:225px;border:4px solid var(--lime);border-radius:14px}
.steps-tag{position:absolute;left:-4px;top:-4px;width:84px;height:225px;background:var(--lime);border-radius:14px 0 0 14px;
  display:flex;flex-direction:column;align-items:center;justify-content:center;font-family:"M PLUS Rounded 1c",sans-serif;
  font-weight:800;font-size:36px;line-height:1.3;color:var(--green-dark)}
.step{position:absolute;top:52px;width:100px;height:100px;border-radius:50%;border:3px solid var(--green);background:var(--white);
  display:flex;flex-direction:column;align-items:center;justify-content:center;text-align:center;font-size:13px;font-weight:700;line-height:1.35}
.step small{font-size:9px;font-weight:400}
.step.filled{background:var(--lime-soft)}
.step-arrow{position:absolute;top:94px;width:16px;height:16px}
.step-note{position:absolute;top:162px;left:640px;width:170px;font-size:9px;line-height:1.45;text-align:center}

.notes{position:absolute;left:14px;top:990px;width:821px}
.notes-tag{display:inline-block;background:var(--green);color:var(--white);font-size:13px;font-weight:700;padding:2px 12px}
.notes ul{list-style:none;margin-top:10px;font-size:12px;line-height:2.2}
.notes li::before{content:"● ";color:var(--green)}
</style>
</head>
<body>
<main class="flyer">
  <div class="top-rule"></div>
  <h1 class="title-tab">植替え</h1>

  <section class="price-panel">
    <p class="price-lead">新しく植え替える鉢の上部直径</p>
    <div class="price-row"><div class="price-size">15cm（5号鉢）まで</div><div class="price-yen">3,500円</div></div>
    <div class="price-row"><div class="price-size">21cm（7号鉢）まで</div><div class="price-yen">6,000円</div></div>
    <div class="price-row"><div class="price-size">30cm（10号鉢）まで</div><div class="price-yen">9,000円</div></div>
    <div class="price-row"><div class="price-size">45cm（15号鉢）まで</div><div class="price-yen">15,000円</div></div>
    <p class="price-note">※ただし、盆栽は除く<br>※（価格はすべて税込み）</p>
  </section>

  <div class="fern-photo" role="img" aria-label="鮮やかな緑のシダの葉の写真"></div>
  <div class="free-badge">お見積り<br>無料</div>
  <p class="one-pot">1鉢からでも承ります！</p>

  <section class="merits">
    <div class="merit">
      <svg style="left:84px;top:16px" width="100" height="100" viewBox="0 0 100 100">
        <rect x="0" y="0" width="100" height="100" rx="8" fill="#fff"/>
        <circle cx="50" cy="50" r="34" fill="#2b2b2b"/>
        <text x="50" y="64" text-anchor="middle" font-size="40" font-weight="700" fill="#fff" font-family="Noto Sans JP,sans-serif">¥</text>
      </svg>
      <div class="merit-label" style="left:16px;right:16px;bottom:18px;text-align:center;font-size:17px">料金は作業代のみ</div>
    </div>
    <div class="merit">
      <svg style="left:20px;top:8px" width="140" height="84" viewBox="0 0 140 90">
        <path d="M10 85 Q40 35 70 85 Z" fill="#fff" stroke="#2b2b2b" stroke-width="3"/>
        <path d="M80 22 H130 L122 85 H88 Z" fill="#fff" stroke="#2b2b2b" stroke-width="3"/>
        <rect x="76" y="14" width="58" height="10" fill="#2b2b2b"/>
      </svg>
      <div class="merit-label" style="left:12px;right:12px;top:96px;font-size:15px">鉢や土など当社で<br>ご用意することも可能。<br>（その場合、別途お見積り）</div>
    </div>
    <div class="merit">
      <svg style="left:12px;top:28px" width="130" height="80" viewBox="0 0 150 100">
        <rect x="10" y="20" width="80" height="55" fill="#fff" stroke="#2b2b2b" stroke-width="3"/>
        <path d="M90 38 H120 L138 55 V75 H90 Z" fill="#fff" stroke="#2b2b2b" stroke-width="3"/>
        <circle cx="35" cy="80" r="11" fill="#2b2b2b"/><circle cx="115" cy="80" r="11" fill="#2b2b2b"/>
      </svg>
      <div class="merit-label" style="right:10px;top:14px;width:110px;text-align:center;font-size:14px">古い土、不要になった鉢のお引き取り可能。<br>（別途見積り）</div>
      <p class="merit-small" style="left:14px;bottom:12px;width:128px">※ただし、プラスチック、金属、ガラス、樹脂、コンクリートなどはお引き取りできません。</p>
    </div>
  </section>

  <section class="services">
    <div class="service">
      <div class="service-head"><span class="service-tag">剪定</span><span class="service-desc">形を整えたり、高さを調整</span></div>
      <div class="service-price"><span>高さ 3m 未満</span><span>4,000 円 / 本</span></div>
    </div>
    <div class="service">
      <div class="service-head"><span class="service-tag">消毒</span><span class="service-desc">病害虫の症状にあわせた薬剤を散布し<br>予防や駆除をします。</span></div>
      <div class="service-price"><span>高さ 3m 未満</span><span>2,000 円 / 本</span></div>
    </div>
    <div class="service">
      <div class="service-head"><span class="service-tag">施肥</span><span class="service-desc">肥料を施して栄養を補い、<br>成育促進、花付き、実付きの改善</span></div>
      <div class="service-price"><span>3,000 円より</span></div>
    </div>
  </section>

  <section class="steps">
    <div class="steps-tag"><span>手</span><span>順</span></div>
    <div class="step" style="left:100px">ご依頼<small>（電話・WEB）</small></div>
    <svg class="step-arrow" style="left:202px" viewBox="0 0 16 16"><path d="M2 2 L14 8 L2 14 Z" fill="#3d9a3a"/></svg>
    <div class="step" style="left:220px">担当から連絡</div>
    <svg class="step-arrow" style="left:322px" viewBox="0 0 16 16"><path d="M2 2 L14 8 L2 14 Z" fill="#3d9a3a"/></svg>
    <div class="step filled" style="left:340px">無料見積り</div>
    <svg class="step-arrow" style="left:442px" viewBox="0 0 16 16"><path d="M2 2 L14 8 L2 14 Z" fill="#3d9a3a"/></svg>
    <div class="step" style="left:460px">ご依頼<small>（作業日時決定）</small></div>
    <svg class="step-arrow" style="left:562px" viewBox="0 0 16 16"><path d="M2 2 L14 8 L2 14 Z" fill="#3d9a3a"/></svg>
    <div class="step filled" style="left:580px">作業</div>
    <svg class="step-arrow" style="left:682px" viewBox="0 0 16 16"><path d="M2 2 L14 8 L2 14 Z" fill="#3d9a3a"/></svg>
    <div class="step" style="left:700px">お支払い</div>
    <p class="step-note">郵便局・銀行振込、コンビニ後払い、<br>クレジットカード決済</p>
  </section>

  <section class="notes">
    <span class="notes-tag">無料見積り</span>
    <ul>
      <li>お客様宅へ出向いて実際のものを見てお見積りをします。見積書有効期限1か月</li>
      <li>植替えで必要な鉢や土などは、お客さまがご用意いただければ別途費用がかからず、そちらを使用して作業致します。</li>
    </ul>
  </section>
</main>
</body>
</html>
```